Modern, crisp, funky web 2.0 site required for childrens holiday programmes

We want a new "Wow" website. Please help this become a reality.

Funtrek is a provider of childrens holiday programmes aimed primary at children 5yrs to 12 yrs. You can view our current site at www.funtrek.co.nz

This website is a primarily a booking portal. Parents typically come to the website to register and book for courses after having seen them in a booklet. However we are changing the marketing approach and are now trying to attract parents directly to the website. Therefore we want the website to be very graphically appealing, very easy to browse and navigate and must be easy to register and book.

The front end is what is being re-designed. The new front end MUST be compatible with the existing back-end system and processes and the back-end should not need to be changed at all. People lodging a tender must familiarise themselves with the existing site and ensure that the new front end will be fully compatible.

The site must be PHP

This tender will not include a re-design of the logo. Please use the current logo which is attached with this document.

Everything else is up for re-design. The site needs a new, clean, crisp modern design. (See Likes and Dislikes).

Some yellow must be used somewhere within the colour scheme to be in keeping with the brand colours. However no yellow background please.

We currently operate in 2 main regions: Auckland and Palmerston North. However we will be adding new regions soon. The website should make it easy for users to find courses in their region easily.

We also offer term time activities – the site needs another area for that. Perhaps emulated as another “region”.

Beyond that courses are offered across a range of activities. Ideally the website would organise courses logically so that users can find what they are looking for easily.

However, if possible it would be good for the user to be able to browse by area. For example within Auckland there would be North Shore, Central, West, East and South. Within each area a range of course are available – e.g. Skateboarding, Surfing etc. However we don’t want this to be the primary design goal. This is more a “could have” than a “must have”

Once the user has found the course they want the site needs to have a course identification button / tab / box e.g. Tennis. Once the user has clicked through all the details pertaining to the tennis courses on offer should be presented. People are used to searching the existing website in this manner.

When clients click through from the course they have chosen to book the GREEN box that’s say “More Info” needs to be changed to say Book Now

Needs to the ability to have photos displayed on each page next to course descriptions or a panel of photos showing the children doing the activity displayed on that page.

Needs the ability to select the “Pick up locations” To show up in the booking form and class attendance sheet e.g. 7.45am/4.45pm: Harbourview Burgerbarn Carpark. In front of Burgerbarn by the shopping trundler bay.
8.10am/4.10pm: Tolley Cove Reserve, Ridgefield Road, Marlowton in the car park in form of the tennis courts

Needs to have Course options above the line (at the top of the page)

Needs to have a description of Funtrek below the line (at the bottom of the page)

You can provide stock images but they must be New Zealand activities (i.e. not American Football) and pre-approved by us. Alternatively we can supply some images.

What adjectives should best describe your website design?
Clean, modern, professional, vibrant, both kid and adult appealing, fun, interesting

What content must be included in the website design?

• Home page
• Contact us
• Testimonials
• Terms and conditions
• New customer sign or log in
• My account or existing client log in
• Chatterbook button,
• Sign up to the newsletter (postparrot)
• Refer a friend option – where they input a friend’s contact details, we then send them a one-off email “from” the friend with a HTML email describing our website. Content of the email must be able to be modified easily later (by a programmer).
• “Become a course provider” enquiry tab. This could be a simple form which emails details through.
• Have “View latest booklet” tab which downloads a PDF of the booklet after submitting the users email address onto our PostParrot mailing list (must offer postparrot integration).
• Must support Zenmetric analytics data collection
Updates

Reason: I have not really seen anything that greatly excites me. I am concerned we re not getting the level of design work in as committed to on the starting up stage we only have 18 designs (Many from the same designer and repeats) I was expecting closer to 50. Please can you assist and advise as to how to improve the results thanks Dana

Target Market(s)

Parents, both working and stay at home, children aged 5-15 years of age with middle – high income.

Industry/Entity Type

Marketing

Requirements
Must have
• The site must be easy to use and navigate.

Users need to be able to navigate with the minimal number of clicks as the site is used by busy mums with no patience!

Users should be able to find exactly what they want with absolute ease.

Needs to be appealing to children aged 5 – 12 years old as well as parents of children within that age range.

Needs to have lots of images of children doing the activities offered. Should NOT have cartoon images!

Must be able to written in PHP – this is to enable it to be compatible with the existing back-end.

Likes:

Big Icons
Clean, crisp design
Vivid, striking in appearance
Uncluttered
Easy to navigate
Social Media integration
Modern
Not much ‘below the line’
Thematically consistent
Easily modifiable pictures and content
Like real images
Search bar would be good if effective ONLY

What colours do you want to see in your website design?
The Yellow in the logo BUT NOT as the background, purple as in the balls etc on logo, white for clean and simple easy to read, black for writing and other areas for details ie boarders etc.
Should not have
• Dislikes:

Cartoon images – must be real images.
Moving, floating in and out and spinning pictures text or photos
Clutter
Underlining
Intentionally misspelt words and typos
Content ‘below the line’ on the Home page
Backgrounds ending before the edge of the screen

What colours do you NOT want to see in your website design?
Browns, pink, pastel colours, mustard, pale yellow, and not a confusion of colours – must be themed and consistent.

```html
<!DOCTYPE html>
<html lang="en">
<head>
<meta charset="utf-8">
<title>Funtrek – A world of fun activities</title>
<link rel="stylesheet" href="https://fonts.googleapis.com/css2?family=Montserrat:wght@400;500;600;700&family=Open+Sans:wght@400;600&family=Schoolbell&display=swap">
<style>
:root{
  --ink:#222;
  --text:#555;
  --muted:#888;
  --rule:#d9d9d9;
  --panel:#f4f4f4;
  --dark:#1b1b1b;
  --dark-2:#3a3a3a;
  --yellow:#f2e30b;
  --red:#9c1020;
  --orange:#c4431a;
  --orange-2:#a9300e;
  --blue:#1686b9;
  --white:#fff;
}
*{box-sizing:border-box;margin:0;padding:0}
html,body{width:1200px;height:2185px;overflow:hidden}
body{position:relative;background:var(--white);font-family:"Open Sans",Arial,sans-serif;color:var(--text)}
.abs{position:absolute}

/* header */
.top-strip{left:0;top:0;width:1200px;height:8px;background:#e6e6e6}
.account-links{left:880px;top:4px;display:flex;gap:4px}
.account-links a{display:block;background:#e8e8e8;color:#333;font:600 12px "Open Sans",sans-serif;padding:5px 9px;text-decoration:none;border-radius:0 0 3px 3px}
.brand{left:150px;top:24px;display:flex;align-items:center;gap:12px}
.brand-dot{width:30px;height:30px;border-radius:50%;background:var(--yellow)}
.brand-name{font:700 52px/1 "Montserrat",sans-serif;color:var(--ink);letter-spacing:-1px}
.brand-tag{left:193px;top:99px;font:500 12px "Montserrat",sans-serif;color:#444;letter-spacing:.3px}
.search{left:670px;top:70px;width:390px;height:48px;background:#6f6f6f;border-radius:5px;padding:7px;display:flex;align-items:center}
.search-field{flex:1;height:34px;background:var(--white);border-radius:3px 0 0 3px;display:flex;align-items:center;padding-left:10px}
.search-btn{width:74px;height:28px;margin-right:4px;background:var(--yellow);font:700 13px "Montserrat",sans-serif;color:#222;display:flex;align-items:center;justify-content:center;position:absolute;right:10px}

.nav{left:0;top:131px;width:1200px;height:44px;background:linear-gradient(#2b2b2b,#111)}
.nav ul{position:absolute;left:142px;top:0;display:flex;list-style:none;height:44px}
.nav li{font:500 16px/44px "Montserrat",sans-serif;color:var(--white);padding:0 18px;border-right:1px solid #555}
.nav li:first-child{padding-left:16px}
.nav li:last-child{border-right:0}
.nav-social{left:984px;top:138px;display:flex;gap:8px}
.nav-social span{width:29px;height:29px;border-radius:50%;background:var(--white)}

.hero{left:0;top:175px;width:1200px;height:468px;background:linear-gradient(100deg,#e9ebee 0%,#f3e35a 22%,#4a9fd1 45%,#f2dc3a 62%,#e8eaec 85%,#d8dadc 100%)}
.hero-caption{left:306px;top:579px;width:590px;height:58px;background:rgba(255,255,255,.75);font:400 38px/58px "Schoolbell",cursive;color:#111;text-align:center}

/* welcome */
.welcome{left:155px;top:680px;width:590px}
.welcome h1{font:400 33px "Montserrat",sans-serif;color:#666;margin-bottom:20px}
.welcome h1 b{color:#222;font-weight:500}
.welcome p{font-size:13px;line-height:20px;margin-bottom:16px}
.welcome h2{font:500 18px "Montserrat",sans-serif;color:#222;margin:20px 0 14px}

.provider{left:777px;top:677px;width:281px;height:264px;background:#efefef;border:1px solid var(--rule)}
.provider-head{height:42px;background:linear-gradient(#3a3a3a,#141414);color:var(--white);font:500 16px/42px "Montserrat",sans-serif;text-align:center}
.field{position:absolute;left:18px;width:246px;height:26px;background:var(--white);border:1px solid #ddd;font-size:11px;color:#555;padding:5px 6px}
.provider-submit{position:absolute;left:18px;top:210px;width:246px;height:33px;background:linear-gradient(#777,#2a2a2a);color:var(--white);font:500 19px/33px "Montserrat",sans-serif;text-align:center;letter-spacing:1px}
.booklet{left:777px;top:955px;width:281px;height:135px;background:linear-gradient(135deg,var(--orange),var(--orange-2));color:var(--white)}
.booklet-text{position:absolute;left:14px;top:12px;font:400 35px/38px "Montserrat",sans-serif}
.booklet-doc{position:absolute;left:173px;top:38px;width:36px;height:48px;background:var(--white);border-radius:2px}
.booklet-doc i{position:absolute;left:-6px;top:26px;width:30px;height:14px;background:#d21d1d}

/* course panels */
.panel{background:var(--panel);border:1px solid var(--rule);border-radius:4px;width:919px;left:141px}
.panel-title{background:var(--white);border:1px solid var(--rule);font:700 23px "Montserrat",sans-serif;color:#111;text-align:center;letter-spacing:.5px;height:42px;line-height:42px}
.tile{position:absolute;width:170px;height:86px;border:2px solid var(--white);box-shadow:0 0 0 1px #ddd}
.tile-label{position:absolute;left:4px;top:6px;background:#111;color:var(--white);font:400 11px/18px "Montserrat",sans-serif;padding:0 7px;text-transform:uppercase}
.tile-label.bottom{top:auto;bottom:6px}
.pager{display:flex;gap:2px}
.pager span{width:24px;height:22px;background:var(--white);border:1px solid #ccc;display:flex;align-items:center;justify-content:center}

/* signup row */
.box{top:1786px;width:292px;height:132px;background:#ececec}
.box-head{height:38px;background:linear-gradient(#3a3a3a,#141414);color:var(--white);font:500 17px/38px "Montserrat",sans-serif;padding-left:12px}
.input{position:absolute;height:24px;background:var(--white);border:1px solid #ddd;font-size:11px;color:#444;padding:4px 7px}
.btn-red{position:absolute;height:24px;background:var(--red);color:var(--white);font:600 12px/24px "Open Sans",sans-serif;padding:0 10px}
.accept{left:766px;top:1786px;width:294px;height:134px;background:var(--blue);color:var(--white);text-align:center}

/* footer */
.footer{left:0;top:1939px;width:1200px;height:246px;background:var(--dark);border-top:8px solid var(--dark-2)}
.foot-h{font:500 13px "Montserrat",sans-serif;color:#ddd;letter-spacing:.5px}
.foot-small{font-size:11px;line-height:15px;color:#999}
.foot-bar{left:141px;top:2145px;width:919px;height:31px;background:#262626;font-size:10px;color:#999;line-height:31px;padding:0 6px}
</style>
</head>
<body>

<div class="abs top-strip"></div>
<div class="abs account-links"><a>REGISTER</a><a>MY ACCOUNT</a></div>

<div class="abs brand"><span class="brand-name">Funtrek</span><span class="brand-dot"></span></div>
<div class="abs brand-tag">A WORLD OF FUN ACTIVITIES</div>

<div class="abs search">
  <div class="search-field">
    <svg width="20" height="20" viewBox="0 0 20 20"><circle cx="8" cy="8" r="6" fill="none" stroke="#888" stroke-width="2.5"/><line x1="12.5" y1="12.5" x2="18" y2="18" stroke="#888" stroke-width="3"/></svg>
  </div>
  <div class="search-btn">SEARCH</div>
</div>

<nav class="abs nav">
  <ul>
    <li>HOME</li><li>COURSES</li><li>TESTIMONIALS</li><li>CONTACT</li><li>TERMS &amp; CONDITIONS</li>
  </ul>
</nav>
<div class="abs nav-social"><span aria-label="Chatterbook"></span><span aria-label="Chirpline"></span></div>

<div class="abs hero" role="img" aria-label="Photo of three children in chef hats and aprons baking together in a bright kitchen"></div>
<div class="abs hero-caption">Funtrek - a world of fun activities!</div>

<section class="abs welcome">
  <h1>Welcome to <b>Funtrek</b></h1>
  <p>With over 100 courses to choose from Funtrek offers a huge range of fun hands on experiences for children aged 4 and older, both in Auckland and Palmerston North.</p>
  <p>Our programmes provide a fantastic opportunity to discover and experience activities your children may never have tried before or they simply just enjoying doing, while encouraging new skills and interests.</p>
  <p>When choosing a Holiday Programmes the safety and happiness of your children is of upmost importance, our courses offer limited student spaces per course along with high instructor /student ratio, making this an enjoyable experience for your children.</p>
  <h2>Make every day of the holidays memorable, make every day fun!</h2>
  <p>If you can't find a programme you are looking for please let us know, and we'll see if we can arrange it for you.</p>
  <p>For full details of our courses click on the course title of interest then all you have to do is select, book and pay online, it's that simple.</p>
</section>

<aside class="abs provider">
  <div class="provider-head">BECOME A COURSE PROVIDER</div>
  <div class="field" style="top:57px">Name</div>
  <div class="field" style="top:90px">Email Address</div>
  <div class="field" style="top:123px;height:74px">Comments</div>
  <div class="provider-submit">SUBMIT</div>
</aside>

<div class="abs booklet">
  <div class="booklet-text">View<br>Latest<br>Booklet</div>
  <div class="booklet-doc"><i></i></div>
  <svg style="position:absolute;left:236px;top:52px" width="26" height="30" viewBox="0 0 26 30"><path d="M3 3l10 12-10 12M12 3l10 12-10 12" fill="none" stroke="#7a1c05" stroke-width="3"/></svg>
</div>

<!-- Auckland -->
<section class="abs panel" style="top:1151px;height:293px">
  <div class="tile" style="left:16px;top:33px;background:linear-gradient(120deg,#f4f4f4,#c44 70%,#333)" role="img" aria-label="Photo of a boy in a suit acting"><span class="tile-label">Acting</span></div>
  <div class="tile" style="left:195px;top:33px;background:linear-gradient(120deg,#b01818,#2a0c0c)" role="img" aria-label="Photo of a magician's hands and hat on red curtains"><span class="tile-label">Magic</span></div>
  <div class="tile" style="left:373px;top:33px;background:linear-gradient(120deg,#e46a6a,#d9c9b3 60%,#3c7a3c)" role="img" aria-label="Photo of children painting at a table"><span class="tile-label">Art</span></div>
  <div class="tile" style="left:552px;top:33px;background:linear-gradient(120deg,#a8c86a,#e24848 50%,#5a8ed0)" role="img" aria-label="Photo of children riding bikes"><span class="tile-label">Bikes</span></div>
  <div class="tile" style="left:730px;top:33px;background:linear-gradient(120deg,#f4f4f4,#f2d33a 55%,#4a9fd1)" role="img" aria-label="Photo of children in chef hats cooking"><span class="tile-label">Cooking</span></div>
  <div class="tile" style="left:16px;top:150px;background:linear-gradient(120deg,#7a5a50,#c85a4a 60%,#3a2a28)" role="img" aria-label="Photo of a couple dancing"><span class="tile-label">Dance</span></div>
  <div class="tile" style="left:195px;top:150px;background:linear-gradient(120deg,#3a6ad0,#d84a4a 50%,#f0c040)" role="img" aria-label="Photo of children in costumes for drama"><span class="tile-label">Drama</span></div>
  <div class="tile" style="left:373px;top:150px;background:linear-gradient(120deg,#f1e6d8,#d8b890)" role="img" aria-label="Photo of a child holding a small pet"><span class="tile-label">Animal Care</span></div>
  <div class="tile" style="left:552px;top:150px;background:linear-gradient(120deg,#4a78b8,#f0a23a 60%,#3a5a90)" role="img" aria-label="Photo of a young gymnast"><span class="tile-label">Gymnastics</span></div>
  <div class="tile" style="left:730px;top:150px;background:linear-gradient(120deg,#2a3a1a,#4c9a2a 50%,#8cc84a)" role="img" aria-label="Photo of a child playing golf on grass"><span class="tile-label">Golf</span></div>
</section>
<div class="abs panel-title" style="left:509px;top:1129px;width:182px">AUCKLAND</div>
<div class="abs pager" style="left:575px;top:1434px">
  <span><svg width="8" height="10"><path d="M7 0L1 5l6 5z" fill="#555"/></svg></span>
  <span><svg width="8" height="10"><path d="M1 0l6 5-6 5z" fill="#1686b9"/></svg></span>
</div>

<!-- Mid term -->
<section class="abs panel" style="top:1539px;height:174px">
  <div class="tile" style="left:18px;top:56px;background:linear-gradient(120deg,#7a9ac0,#6a4a30 55%,#3a2a1a)" role="img" aria-label="Photo of a child horse riding"><span class="tile-label bottom">Horseriding Hillcrest<br>Riding Sch</span></div>
  <div class="tile" style="left:195px;top:56px;background:linear-gradient(120deg,#f6ead0,#e0b84a 55%,#c89a20)" role="img" aria-label="Photo of gold jewellery"><span class="tile-label bottom">Jewellery</span></div>
  <div class="tile" style="left:377px;top:56px;background:linear-gradient(180deg,#2a6ab8,#5a9ad8 60%,#c86a30)" role="img" aria-label="Photo of a netball hoop against blue sky"><span class="tile-label bottom">Netball</span></div>
  <div class="tile" style="left:554px;top:56px;background:linear-gradient(120deg,#d8c8b0,#8a6a50 55%,#e0d0c0)" role="img" aria-label="Photo of children playing soccer"><span class="tile-label bottom">KickstartTots</span></div>
  <div class="tile" style="left:732px;top:56px;background:linear-gradient(120deg,#4a8a6a,#2f6a50)" role="img" aria-label="Photo of a green chalkboard"><span class="tile-label bottom">Lorem Ipsum</span></div>
</section>
<div class="abs panel-title" style="left:443px;top:1517px;width:314px">MID TERM ACTIVITIES</div>
<div class="abs pager" style="left:575px;top:1703px">
  <span><svg width="8" height="10"><path d="M7 0L1 5l6 5z" fill="#555"/></svg></span>
  <span><svg width="8" height="10"><path d="M1 0l6 5-6 5z" fill="#1686b9"/></svg></span>
</div>

<!-- Signup row -->
<div class="abs box" style="left:141px">
  <div class="box-head">NEWSLETTER</div>
  <div style="position:absolute;left:16px;top:54px;font-size:11px;color:#444">Sign up to the newsletter</div>
  <div class="input" style="left:11px;top:88px;width:186px">Enter your email</div>
  <div class="btn-red" style="left:205px;top:88px">SUBMIT</div>
</div>
<div class="abs box" style="left:453px">
  <div class="box-head">REFER A FRIEND</div>
  <div class="input" style="left:11px;top:54px;width:186px">Your name</div>
  <div class="input" style="left:11px;top:88px;width:186px">Enter your email</div>
  <div class="btn-red" style="left:205px;top:88px">SUBMIT</div>
</div>
<div class="abs accept">
  <div style="position:absolute;left:12px;top:12px;width:40px;height:26px;background:#f0b040;border-radius:3px"></div>
  <div style="position:absolute;left:84px;top:10px;font:400 21px 'Montserrat',sans-serif">We Accept</div>
  <div style="position:absolute;left:10px;top:44px;width:274px;font-size:11px;line-height:14px">We accept Cardwise and Paymaster or for more assistance please call the office on:</div>
  <div style="position:absolute;left:0;top:76px;width:294px;font:500 17px/22px 'Montserrat',sans-serif">Auckland <b>555 0142</b><br>Palmerston North <b>555 0199</b></div>
</div>

<!-- Footer -->
<footer class="abs footer">
  <div class="abs foot-h" style="left:142px;top:32px">QUESTIONS? CALL</div>
  <div class="abs" style="left:142px;top:58px;font:400 24px 'Montserrat',sans-serif;color:#777">(844) 555-0187</div>
  <div class="abs" style="left:178px;top:136px;width:40px;height:40px;border-radius:50%;background:#666"></div>
  <div class="abs" style="left:228px;top:144px;font:400 19px 'Open Sans',sans-serif;color:#e8a020">enquiries@funtrek.co.nz</div>

  <div class="abs foot-h" style="left:352px;top:32px">CONNECT WITH US</div>
  <div class="abs" style="left:354px;top:64px;width:28px;height:28px;background:#3b5a9a;border-radius:3px" aria-label="Chatterbook"></div>
  <div class="abs" style="left:398px;top:64px;width:28px;height:28px;background:#3aaae0;border-radius:3px" aria-label="Chirpline"></div>
  <div class="abs" style="left:442px;top:64px;width:28px;height:28px;background:#f08a20;border-radius:3px" aria-label="Feed"></div>

  <div class="abs foot-h" style="left:536px;top:32px">WE ACCEPT</div>
  <div class="abs foot-small" style="left:536px;top:58px;width:240px">We accept Cardwise and Paymaster or for more assistance please call the office on:</div>
  <div class="abs" style="left:536px;top:94px;font:400 18px/28px 'Montserrat',sans-serif;color:#ddd">Auckland 555 0142<br>Palmerston North 555 0199</div>

  <div class="abs foot-h" style="left:808px;top:32px">CONTACT US</div>
  <svg class="abs" style="left:810px;top:56px" width="14" height="20" viewBox="0 0 14 20"><path d="M7 0a7 7 0 0 1 7 7c0 5-7 13-7 13S0 12 0 7a7 7 0 0 1 7-7z" fill="#888"/><circle cx="7" cy="7" r="2.6" fill="#1b1b1b"/></svg>
  <div class="abs foot-small" style="left:836px;top:56px;width:220px">Auckland 555 0142<br>Palmerston North 555 0199<br>enquiries@funtrek.co.nz<br><b style="color:#ccc">Postal:</b><br>P O Box 402, Fernvale, Auckland 0799<br><b style="color:#ccc">Office:</b><br>Harlow Road, Auckland 0799</div>
</footer>
<div class="abs foot-bar">TERMS &amp; CONDITIONS &nbsp;|&nbsp; PRIVACY POLICY &nbsp;|&nbsp; SITE MAP<span style="float:right">COPYRIGHT © 2012 FUNTREK, ALL RIGHTS RESERVED.</span></div>

</body>
</html>
```